Flyer for Custom Home Builder!

my company is Harlow Ridge Homes, I am looking for a flyer that we can send via email to a customer, or print and hand out. I am thinking four pages so we could print this and fold it., possibly creating a folder. The name of the company is Harlow Ridge Homes our website is here www.harlowridgehomes-example.com. Some text you can use "Crafting luxury homes isn't just a job, it's our passion.
With meticulous attention to detail and an unwavering commitment to using the finest materials, Harlow Ridge Homes consistently delivers exceptional results that stand as a testament to our commitment to quality."

"Trust is the cornerstone of our foundation.
With a proven track record of delivering on our promises for over 16 years, we prioritize transparent communication and integrity throughout every step of the home-building journey".

you may need to obtain the photos here
https://files.example-share.net/f/k27pw4m8zrt03xq61bnv/h?key=48vn2c9q1x7mb5t0ekd3h&dl=0

Target Market(s)

We build homes for every wealthy clients, therefore the photos are extremely important

Industry/Entity Type

Construction.

Requirements
Must have
• clear larger photos

```html
<!DOCTYPE html>
<html lang="en">
<head>
<meta charset="utf-8">
<title>Harlow Ridge Homes – Folded Flyer</title>
<link rel="stylesheet" href="https://fonts.googleapis.com/css2?family=Montserrat:ital,wght@0,400;0,500;0,700;0,800;1,400&display=swap">
<style>
  :root {
    --page-bg: #ffffff;
    --panel-dark: #1b1b1b;
    --text-light: #f2f2f2;
    --mark-grey: #8a8a8a;
    --mark-grey-dark: #6f6f6f;
    --sheet-white: #ffffff;
  }
  * { margin: 0; padding: 0; box-sizing: border-box; }
  html, body {
    width: 872px; height: 1200px; overflow: hidden;
    background: var(--page-bg);
    font-family: "Montserrat", Arial, sans-serif;
  }
  .canvas { position: relative; width: 872px; height: 1200px; }

  .spread {
    position: absolute; left: 66px; width: 740px;
    box-shadow: 0 2px 10px rgba(0,0,0,0.18);
    overflow: hidden;
  }
  .spread--outside { top: 31px; height: 523px; background: var(--panel-dark); }
  .spread--inside { top: 605px; height: 524px; background: var(--sheet-white); }

  .wordmark {
    position: absolute; white-space: nowrap; text-align: center;
    font-weight: 800; text-transform: uppercase; color: var(--mark-grey);
    line-height: 1;
  }

  /* outside spread – back panel */
  .back-panel { position: absolute; left: 0; top: 0; width: 370px; height: 523px; }
  .back-panel .wordmark { left: 0; width: 370px; top: 156px; font-size: 15px; letter-spacing: 1.5px; }
  .invite {
    position: absolute; left: 10px; width: 350px; top: 200px;
    color: var(--text-light); font-size: 10.6px; line-height: 11.4px; text-align: center;
    white-space: nowrap;
  }
  .invite strong { font-weight: 700; }
  .contact-list { position: absolute; left: 58px; top: 377px; width: 300px; height: 120px; color: var(--text-light); font-size: 11px; }
  .contact-row { position: absolute; display: flex; align-items: center; white-space: nowrap; }
  .contact-row svg { flex: none; }
  .contact-row--phone { top: 0; left: 0; }
  .contact-row--phone span { margin-left: 12px; }
  .contact-row--address { top: 26px; left: 3px; }
  .contact-row--address span { margin-left: 17px; line-height: 11.6px; }
  .contact-row--email { top: 55px; left: 1px; }
  .contact-row--email span { margin-left: 15px; }
  .contact-row--hours { top: 85px; left: 50px; }
  .contact-row--hours span { margin-left: 11px; line-height: 14px; }
  .contact-row--hours b { font-weight: 500; }

  /* outside spread – cover panel */
  .cover-photo {
    position: absolute; left: 370px; top: 0; width: 370px; height: 394px;
    background: linear-gradient(180deg, #9db8d4 0%, #7f9fbf 40%, #5c7c98 62%, #3e5870 82%, #2c3b4b 100%);
  }
  .cover-panel .wordmark {
    left: 395px; width: 224px; top: 443px; font-size: 20px; letter-spacing: 0.5px;
  }

  /* inside spread */
  .feature-photo {
    position: absolute; left: 0; top: 0; width: 296px; height: 524px;
    background: linear-gradient(180deg, #7f9fc0 0%, #a9bccd 48%, #9a8a72 62%, #6f6a52 74%, #6b6a3f 100%);
  }
  .inside-wordmark.wordmark { left: 296px; width: 444px; top: 27px; font-size: 14px; letter-spacing: 0.5px; color: var(--mark-grey-dark); }
  .message-box {
    position: absolute; left: 200px; width: 530px; background: var(--panel-dark);
    color: var(--text-light); font-style: italic; font-size: 10.6px; line-height: 11.4px; text-align: center;
    white-space: nowrap;
  }
  .message-box p { position: absolute; left: 0; right: 0; }
  .message-box--passion { top: 77px; height: 101px; }
  .message-box--passion p { top: 24px; }
  .message-box--trust { top: 358px; height: 106px; }
  .message-box--trust p { top: 26px; }
  .gallery { position: absolute; left: 200px; top: 178px; width: 530px; height: 180px; display: flex; }
  .gallery-photo { height: 180px; }
  .gallery-photo--pool { width: 138px; background: linear-gradient(180deg, #7aa6d2 0%, #cfcdc6 40%, #8f8d86 58%, #86c6d2 78%, #a9b3b5 100%); }
  .gallery-photo--kitchen { width: 140px; background: linear-gradient(180deg, #f3f3f1 0%, #e2e1dd 50%, #2f3442 68%, #6a6560 100%); }
  .gallery-photo--cellar { width: 113px; background: linear-gradient(90deg, #1b4fd6 0%, #3a86f2 45%, #1d4ccc 70%, #1638a6 100%); }
  .gallery-photo--stairs { width: 139px; background: linear-gradient(100deg, #b98a5e 0%, #e8e5e0 45%, #c9c6c0 70%, #a8794f 100%); }
</style>
</head>
<body>
<main class="canvas">

  <section class="spread spread--outside" aria-label="Outside spread">
    <div class="back-panel">
      <div class="wordmark">Harlow Ridge Homes</div>
      <p class="invite">Ready to turn your dream home into a reality?<br>Let's start building together. Visit our website<br>at <strong>www.harlowridgehomes-example.com</strong> to explore our<br>portfolio and discover the art of luxury living.</p>
      <div class="contact-list">
        <div class="contact-row contact-row--phone">
          <svg width="22" height="22" viewBox="0 0 22 22" aria-hidden="true"><circle cx="11" cy="11" r="11" fill="#fff"/><path d="M7.5 5.5c.6-.4 1.3-.3 1.7.3l1 1.6c.3.5.2 1.1-.2 1.5l-.7.6c.6 1.3 1.6 2.4 2.9 3.1l.6-.7c.4-.4 1-.5 1.5-.2l1.6 1c.6.4.7 1.1.3 1.7l-.6.8c-.6.7-1.6.9-2.5.5-2.8-1.3-5-3.5-6.2-6.3-.4-.9-.2-1.9.5-2.5z" fill="#1b1b1b"/></svg>
          <span>(555) 014-2286</span>
        </div>
        <div class="contact-row contact-row--address">
          <svg width="16" height="22" viewBox="0 0 16 22" aria-hidden="true"><path d="M8 0C3.6 0 0 3.5 0 7.8 0 13.5 8 22 8 22s8-8.5 8-14.2C16 3.5 12.4 0 8 0z" fill="#fff"/><circle cx="8" cy="7.8" r="3" fill="#1b1b1b"/></svg>
          <span>480 CEDAR BLUFF LANE,<br>SUITE 100, AUSTIN TX 78700</span>
        </div>
        <div class="contact-row contact-row--email">
          <svg width="21" height="16" viewBox="0 0 21 16" aria-hidden="true"><rect width="21" height="16" rx="2" fill="#fff"/><path d="M2.5 3l8 6 8-6" fill="none" stroke="#1b1b1b" stroke-width="1.5"/></svg>
          <span>info@harlowridge-example.com</span>
        </div>
        <div class="contact-row contact-row--hours">
          <svg width="26" height="26" viewBox="0 0 26 26" aria-hidden="true"><circle cx="13" cy="13" r="13" fill="#fff"/><path d="M12 6.5v7l4 3" fill="none" stroke="#1b1b1b" stroke-width="2.2" stroke-linecap="round"/></svg>
          <span>OPENING HOURS<br><b>MON - FRI, 9 AM - 5 PM</b></span>
        </div>
      </div>
    </div>
    <div class="cover-panel">
      <div class="cover-photo" role="img" aria-label="Modern white luxury home at dusk with glowing glass doors reflected in an infinity pool"></div>
      <div class="wordmark">Harlow Ridge Homes</div>
    </div>
  </section>

  <section class="spread spread--inside" aria-label="Inside spread">
    <div class="feature-photo" role="img" aria-label="Stone-and-timber custom home with porch columns, lawn in front and evening sky"></div>
    <div class="inside-wordmark wordmark">Harlow Ridge Homes</div>
    <div class="message-box message-box--passion">
      <p>Crafting luxury homes isn't just a job, it's our passion.<br>With meticulous attention to detail and an unwavering commitment<br>to using the finest materials, Harlow Ridge Homes consistently<br>delivers exceptional results that stand as a testament to our<br>commitment to quality.</p>
    </div>
    <div class="gallery">
      <div class="gallery-photo gallery-photo--pool" role="img" aria-label="Modern patio with outdoor fireplace and plunge pool"></div>
      <div class="gallery-photo gallery-photo--kitchen" role="img" aria-label="White kitchen with island seating and pendant lights"></div>
      <div class="gallery-photo gallery-photo--cellar" role="img" aria-label="Blue-lit glass wine display wall"></div>
      <div class="gallery-photo gallery-photo--stairs" role="img" aria-label="Floating staircase with glass railing"></div>
    </div>
    <div class="message-box message-box--trust">
      <p>Trust is the cornerstone of our foundation.<br>With a proven track record of delivering on our promises for over 16 years,<br>we prioritize transparent communication and integrity throughout every<br>step of the home-building journey</p>
    </div>
  </section>

</main>
</body>
</html>
```